Product flyer with pricing

We manufacture iconic and luxury vending trailers. for our first trailer we need a flyer created to give to prospective clients with base pricing. I am uploading an example along with graphic files.

```html
<!DOCTYPE html>
<html lang="en">
<head>
<meta charset="utf-8">
<title>Prairie Cottage Mini – Product Flyer</title>
<link rel="stylesheet" href="https://fonts.googleapis.com/css2?family=Open+Sans:wght@400;600;700&family=Ubuntu:wght@500;700&display=swap">
<style>
  :root{
    --green:#62a446;
    --orange:#e39a10;
    --dark:#555555;
    --light:#ececec;
    --white:#ffffff;
    --text:#2a2a2a;
    --muted:#7a7a7a;
    --stage:#e6e6e6;
  }
  *{box-sizing:border-box;margin:0;padding:0}
  html,body{width:671px;height:1200px;overflow:hidden;background:var(--stage)}
  body{font-family:"Open Sans",Arial,sans-serif;color:var(--text)}
  .flyer{position:absolute;left:20px;top:153px;width:631px;height:893px;background:var(--white);overflow:hidden;box-shadow:0 6px 18px rgba(0,0,0,.25)}
  .bg-shapes{position:absolute;left:0;top:0}
  .logo-disc{position:absolute;left:17px;top:-18px;width:254px;height:254px;border-radius:50%;background:var(--white);display:flex;align-items:center;justify-content:center;gap:8px}
  .logo-mark{width:16px;height:16px;border-radius:50%;background:var(--green);flex-shrink:0}
  .logo-name{font-family:"Ubuntu",Arial,sans-serif;font-weight:700;font-size:24px;color:var(--green);letter-spacing:.5px}
  .photo{position:absolute;border-radius:50%;border:4px solid var(--white);background:linear-gradient(180deg,#4d8fe0 0%,#9cc3ee 40%,#f1f2f2 55%,#8f9296 100%)}
  .photo-hero{left:333px;top:17px;width:278px;height:278px}
  .photo-side{left:281px;top:142px;width:90px;height:90px}
  .photo-open{left:15px;top:194px;width:144px;height:144px}
  .photo-rear{left:167px;top:171px;width:118px;height:118px}
  .title{position:absolute;left:150px;width:364px;text-align:center;top:285px}
  .title .pre{font-size:21px;color:var(--muted);line-height:24px}
  .title .name{font-family:"Ubuntu",Arial,sans-serif;font-weight:700;font-size:24px;color:var(--orange);line-height:24px}
  .title .sub{font-size:21px;color:var(--muted);line-height:26px}
  .band{position:absolute;display:flex;align-items:center;justify-content:center;font-family:"Ubuntu",Arial,sans-serif;font-weight:700;color:var(--white);text-transform:uppercase;white-space:nowrap}
  .price-band{left:117px;top:368px;width:378px;height:42px;background:var(--green);clip-path:polygon(5% 0,100% 0,95% 100%,0 100%);font-size:29px}
  .features-band{left:170px;top:410px;width:272px;height:42px;background:var(--orange);clip-path:polygon(7% 0,100% 0,93% 100%,0 100%);font-size:20px}
  .list{position:absolute;list-style:none;font-size:11px;line-height:15px}
  .list li{position:relative;padding-left:18px;margin-bottom:6px}
  .ticks li::before{content:"";position:absolute;left:0;top:3px;width:9px;height:9px;border-radius:50%;background:var(--green)}
  .ticks li::after{content:"";position:absolute;left:3px;top:4.5px;width:2px;height:4px;border:solid var(--white);border-width:0 1.3px 1.3px 0;transform:rotate(45deg)}
  .features-left{left:37px;top:471px;width:258px}
  .features-right{left:337px;top:471px;width:280px}
  .options{position:absolute;left:0;top:581px;width:631px;height:139px;background:var(--dark)}
  .options-band{left:177px;top:0;width:279px;height:40px;background:var(--green);clip-path:polygon(0 0,100% 0,94% 100%,6% 100%);font-size:20px}
  .dots{color:#f2f2f2}
  .dots li{margin-bottom:3px}
  .dots li::before{content:"";position:absolute;left:0;top:3px;width:9px;height:9px;border-radius:50%;background:var(--orange)}
  .price{color:var(--orange);font-weight:700}
  .options-left{left:37px;top:63px;width:205px}
  .options-right{left:337px;top:63px;width:230px}
  .uses{position:absolute;left:0;top:720px;width:631px;height:125px;background:var(--light)}
  .uses-band{left:222px;top:0;width:185px;height:40px;background:var(--orange);clip-path:polygon(0 0,100% 0,90% 100%,10% 100%);font-size:20px}
  .case{position:absolute;font-size:11px;line-height:15px}
  .case b{color:var(--orange);font-weight:700}
  .case.green b{color:var(--green)}
  .case-food{left:37px;top:57px;width:215px}
  .case-retail{left:38px;top:93px;width:185px}
  .case-corporate{left:337px;top:57px;width:225px}
  .case-fundraisers{left:337px;top:95px;width:270px}
  .footer{position:absolute;left:0;top:845px;width:631px;height:48px;background:var(--orange)}
  .footer-shape{position:absolute;left:0;top:0}
  .foot-item{position:absolute;display:flex;align-items:center;gap:7px;color:var(--white);white-space:nowrap}
  .foot-item svg{flex-shrink:0}
  .address{left:37px;top:8px;font-size:11.5px;line-height:16px;align-items:flex-start}
  .address svg{margin-top:2px}
  .web{left:215px;top:16px;font-size:11.5px;line-height:16px}
  .web strong{font-weight:700}
  .phone{left:438px;top:11px;font-family:"Ubuntu",Arial,sans-serif;font-weight:700;font-size:20px;line-height:26px}
</style>
</head>
<body>
<main class="flyer">
  <svg class="bg-shapes" width="631" height="300" viewBox="0 0 631 300" aria-hidden="true">
    <polygon points="0,0 631,0 631,218 600,245 300,215 0,187" fill="var(--green)"/>
    <polygon points="0,187 40,200 0,238" fill="var(--orange)"/>
    <polygon points="631,218 600,245 631,262" fill="var(--orange)"/>
  </svg>

  <div class="logo-disc">
    <span class="logo-mark"></span>
    <span class="logo-name">Little Sun Builds</span>
  </div>

  <div class="photo photo-hero" role="img" aria-label="Photo of the white cottage-style vending house with black door under a blue sky"></div>
  <div class="photo photo-side" role="img" aria-label="Photo of the vending trailer seen from the side"></div>
  <div class="photo photo-open" role="img" aria-label="Photo of the trailer with its serving window opened"></div>
  <div class="photo photo-rear" role="img" aria-label="Photo of the vending house on its tandem-wheel trailer"></div>

  <header class="title">
    <p class="pre">The</p>
    <h1 class="name">"Prairie Cottage Mini"</h1>
    <p class="sub">Luxury, mobile vending house</p>
  </header>

  <div class="band price-band">Base price: $45,000</div>
  <div class="band features-band">Base unit features:</div>

  <ul class="list ticks features-left">
    <li>Trailer features tandem wheels w/ brakes</li>
    <li>Steel frame construction for fire retardation safety and weightreduction.</li>
    <li>100% off grid with solar and lithium battery system allowing the trailer to be used in places not accessible by traditional trailers.</li>
  </ul>
  <ul class="list ticks features-right">
    <li>80 gallon water supply tank</li>
    <li>100 gallon waste water tank</li>
    <li>Cupboards, cabinets &amp; four stainless steel sinks.</li>
    <li>60” Gas shock serving window</li>
  </ul>

  <section class="options">
    <div class="band options-band">Available options:</div>
    <ul class="list dots options-left">
      <li>HVAC - Norvane Mini Split - <span class="price">$1,800</span></li>
      <li>Cooler / Glass front Commercial refrigerator - <span class="price">$1,600</span></li>
      <li>Upper loft storage area - <span class="price">$1,200</span></li>
    </ul>
    <ul class="list dots options-right">
      <li>Signage and graphics - <span class="price">$2,000 - $5,000</span> depend on complexity</li>
      <li>Ice machine - <span class="price">$1,100</span></li>
      <li>Other custom items available on request.</li>
    </ul>
  </section>

  <section class="uses">
    <div class="band uses-band">Use cases:</div>
    <p class="case case-food"><b>Food:</b> Lemonade, Coffee, pizza, cookies, doughnuts, barbecue and more!</p>
    <p class="case green case-retail"><b>Retail:</b> Clothing, watches, jewelry, flowers and more!</p>
    <p class="case case-corporate"><b>Corporate:</b> Product info, demonstration, information, brand awareness.</p>
    <p class="case case-fundraisers"><b>Fundraisers:</b> Girls/boy sports, non profits, etc.</p>
  </section>

  <footer class="footer">
    <svg class="footer-shape" width="631" height="48" viewBox="0 0 631 48" aria-hidden="true">
      <polygon points="198,0 425,0 410,48 183,48" fill="var(--green)"/>
    </svg>
    <div class="foot-item address">
      <svg width="9" height="12" viewBox="0 0 9 12" aria-hidden="true"><path d="M4.5 0A4.5 4.5 0 0 0 0 4.5C0 8 4.5 12 4.5 12S9 8 9 4.5A4.5 4.5 0 0 0 4.5 0z" fill="#fff"/><circle cx="4.5" cy="4.5" r="1.7" fill="var(--orange)"/></svg>
      <span>42 Elmwood Lane,<br>London, N4 2QP</span>
    </div>
    <div class="foot-item web">
      <svg width="11" height="11" viewBox="0 0 12 12" aria-hidden="true"><g fill="none" stroke="#fff" stroke-width="1"><circle cx="6" cy="6" r="5.3"/><ellipse cx="6" cy="6" rx="2.4" ry="5.3"/><line x1="0.7" y1="6" x2="11.3" y2="6"/></g></svg>
      <span>www.<strong>littlesunbuilds</strong>.com</span>
    </div>
    <div class="foot-item phone">
      <svg width="22" height="22" viewBox="0 0 22 22" aria-hidden="true"><circle cx="11" cy="11" r="11" fill="#fff"/><path d="M7.5 5.5l2 2.6-1.2 1.3c.7 1.6 2 2.9 3.5 3.6l1.3-1.2 2.6 2-.9 2c-4.4-.3-8.3-4.2-8.6-8.6z" fill="var(--orange)"/></svg>
      <span>456-555-0192</span>
    </div>
  </footer>
</main>
</body>
</html>
```